Car Soap Label Design specifically targeting RVs

I am private labeling a car wash soap to specifically target the RV industry. It will be sold in a one gallon jug with a 6"x11" spot to place the label on front and wrap around the two sides. (see attached pics for example of label size) The front of the label I want to have a realistic picture of a high dollar class A RV somehow integrated into the design, and the key features of the soap. I had wordsmithbot design a couple that I kind of like the look of that I will attach, but open to other options. I want something clean and professional looking that will back the premium product I am selling.
The name of my brand is "Blue Harbor Gleam". I want the brand name to be somewhere on the label, but not a main focus. I want the focus to be the product and its benefits. "Premium RV Wash and Wax" as the main verbiage. Benefits... "Developed for Use With Foam Gun or Bucket with Water", "Safe for All RV Exteriors", "Protective Wax Formula", "Enhanced Shine", "Water Repellent", "Streak Free Rinse", "UV Protection". On the side...Directions: 2 Ways of Mixing... Pour Concentrate into Foam Gun Bottle OR Mixing Ratio: 1 Part Wash & Wax / 3 Parts Water in bucket. Apply soap to one side of RV at a time and use carwash brush to easily loosen road film and rinse clean. On the other side... Keep from freezing, Keep Out of Reach of Children. MADE IN USA. Hazardous Ingredients: NONE . NOTICE: The seller and/or manufacturer assumes no responsibility for damage or injury resulting from misuse of this product. No warranties, expressed or implied, are given for the performance or safety of this product.

Target Market(s)

RV industry

Industry/Entity Type

RV/Auto

Requirements
Must have
• Clean, Professional look, size 6" tall and 11" wide
Nice to have
• Realistic Class A RV as part of design

```html
<!DOCTYPE html>
<html lang="en">
<head>
<meta charset="utf-8">
<title>Premium RV Wash and Wax – Label</title>
<link href="https://fonts.googleapis.com/css2?family=Montserrat:wght@400;500;600;700;800;900&display=swap" rel="stylesheet">
<style>
:root{
  --page:#e9e9ea;
  --blue:#1c74c6;
  --blue-bright:#1a9ae6;
  --blue-deep:#0f3f7c;
  --navy:#1d4f86;
  --ink:#4a4d52;
  --silver-1:#f4f5f6;
  --silver-2:#d6d8db;
  --steel-1:#8c8f94;
  --steel-2:#3c3f44;
  --white:#ffffff;
}
*{box-sizing:border-box;margin:0;padding:0}
html,body{width:667px;height:1200px;overflow:hidden;background:var(--page);font-family:"Montserrat",sans-serif}
.canvas{position:relative;width:667px;height:1200px}
.label{position:absolute;left:13px;top:425px;width:640px;height:349px;overflow:hidden;
  background:linear-gradient(180deg,var(--silver-1) 0%,var(--silver-2) 62%,var(--steel-1) 78%,var(--steel-2) 100%);
  box-shadow:0 6px 16px rgba(0,0,0,.28)}
.top-band{position:absolute;left:0;top:0;width:100%;height:13px;
  background:linear-gradient(90deg,var(--blue-deep),var(--blue-bright) 50%,var(--blue-deep));
  border-bottom:2px solid var(--blue-bright)}
/* left panel */
.directions{position:absolute;left:0;top:13px;width:148px;height:336px;text-align:center}
.pill{position:absolute;left:22px;top:52px;width:109px;height:19px;border-radius:10px;
  background:var(--navy);border:1.5px solid var(--blue-bright);color:var(--white);
  font-weight:700;font-size:11px;line-height:16px;letter-spacing:.3px}
.ways{position:absolute;left:16px;top:78px;display:flex;align-items:center;gap:3px;color:var(--blue)}
.ways .num{font-size:44px;font-weight:900;line-height:1}
.ways .words{text-align:left;line-height:.95}
.ways .w1{display:block;font-size:23px;font-weight:900}
.ways .w2{display:block;font-size:14px;font-weight:800}
.mix{position:absolute;left:8px;top:133px;width:132px;color:var(--blue);font-size:6.6px;font-weight:700;line-height:1.45}
.apply{position:absolute;left:10px;top:177px;width:128px;color:var(--ink);font-size:6.6px;font-weight:500;line-height:1.45}
.mini-rv{position:absolute;left:13px;top:216px;width:125px;height:60px;border-radius:4px;
  background:linear-gradient(160deg,#5fa0dc 0%,#2a66b3 55%,#9ea3aa 100%)}
.side-name{position:absolute;left:0;top:296px;width:148px;color:var(--white);line-height:1}
.side-name .a{display:block;font-size:14px;font-weight:900;text-shadow:0 1px 2px rgba(0,0,0,.5)}
.side-name .b{display:block;font-size:9.5px;font-weight:700;margin-top:1px}
/* front */
.photo{position:absolute;left:148px;top:13px;width:345px;height:336px;
  background:linear-gradient(180deg,#b9c9d6 0%,#e8d9bf 30%,#6e8a78 45%,#4d7fbe 58%,#3c66a6 72%,#6f7277 86%,#3d4045 100%)}
.title-banner{position:absolute;left:148px;top:13px;width:345px;height:102px}
.title{position:absolute;left:148px;top:28px;width:345px;text-align:center;color:var(--white);line-height:1}
.title .t1{display:block;font-size:31px;font-weight:900;letter-spacing:-.3px;text-shadow:0 2px 2px rgba(0,0,0,.35)}
.title .t2{display:block;font-size:21px;font-weight:800;margin-top:1px;text-shadow:0 2px 2px rgba(0,0,0,.35)}
.title .brand{display:block;font-size:7.5px;font-weight:700;letter-spacing:3.6px;margin-top:6px}
.features{position:absolute;left:148px;top:293px;width:345px;display:flex;justify-content:space-around;padding:0 12px}
.feature{text-align:center;color:var(--white);font-size:10px;font-weight:600;line-height:1.15}
.feature svg{display:block;margin:0 auto 3px}
/* right panel */
.specs{position:absolute;left:493px;top:13px;width:147px;height:336px}
.benefits{position:absolute;left:9px;top:36px;list-style:none}
.benefits li{display:flex;gap:8px;color:var(--ink);font-size:6.9px;font-weight:700;line-height:1.1;margin-bottom:7px}
.benefits li svg{flex:none;margin-top:1px}
.warnings{position:absolute;left:8px;top:150px;list-style:none}
.warnings li{display:flex;align-items:center;gap:5px;color:var(--ink);font-size:7.4px;font-weight:700;line-height:1.1;margin-bottom:7px}
.hazard{position:absolute;left:9px;top:202px;color:var(--blue);font-size:7.4px;font-weight:700}
.notice{position:absolute;left:15px;top:207px;width:113px;height:87px;margin-top:8px;border-radius:5px;
  background:var(--blue);color:var(--white);text-align:center;font-size:6.1px;font-weight:600;line-height:1.3;padding:8px 4px}
.made{position:absolute;left:0;top:309px;width:147px;text-align:center;color:var(--white);font-size:10px;font-weight:700}
</style>
</head>
<body>
<div class="canvas">
  <section class="label">
    <div class="top-band"></div>

    <div class="directions">
      <div class="pill">DIRECTIONS</div>
      <div class="ways"><span class="num">2</span><span class="words"><span class="w1">WAYS</span><span class="w2">OF MIXING</span></span></div>
      <p class="mix">Pour Concentrate into<br>Foam Gun Bottle OR Mixing Ratio:<br>1 Part Wash &amp; Wax / 32 Parts<br>Water in bucket.</p>
      <p class="apply">Apply soap to one side of RV<br>at a time and use carwash brush<br>to easily loosen road film and<br>rinse clean.</p>
      <div class="mini-rv" role="img" aria-label="Photo of a blue and white Class A motorhome"></div>
      <div class="side-name"><span class="a">PREMIUM RV</span><span class="b">WASH AND WAX</span></div>
    </div>

    <div class="photo" role="img" aria-label="Photo of a luxury blue Class A motorhome on a road with mountains and sunset sky"></div>
    <svg class="title-banner" viewBox="0 0 345 102" aria-hidden="true">
      <defs><linearGradient id="bannerFill" x1="0" y1="0" x2="0" y2="1">
        <stop offset="0" stop-color="#1a9ae6"/><stop offset="1" stop-color="#0f4f96"/></linearGradient></defs>
      <path d="M-2 0 H347 V4 C320 6 305 14 292 40 C278 70 268 88 240 92 H108 C80 88 70 70 56 40 C43 14 28 6 -2 4 Z" fill="url(#bannerFill)" stroke="#ffffff" stroke-width="2.5"/>
    </svg>
    <h1 class="title"><span class="t1">PREMIUM RV</span><span class="t2">WASH AND WAX</span><span class="brand">BLUE HARBOR GLEAM</span></h1>
    <div class="features">
      <div class="feature"><svg width="12" height="12" viewBox="0 0 12 12"><circle cx="6" cy="6" r="6" fill="#fff"/><path d="M3.2 6.2l2 2 3.8-4" stroke="#555" stroke-width="1.4" fill="none"/></svg>SAFE FOR ALL RV<br>EXTERIORS</div>
      <div class="feature"><svg width="12" height="12" viewBox="0 0 12 12"><circle cx="6" cy="6" r="6" fill="#fff"/><path d="M3.2 6.2l2 2 3.8-4" stroke="#555" stroke-width="1.4" fill="none"/></svg>UV<br>PROTECTION</div>
      <div class="feature"><svg width="12" height="12" viewBox="0 0 12 12"><circle cx="6" cy="6" r="6" fill="#fff"/><path d="M3.2 6.2l2 2 3.8-4" stroke="#555" stroke-width="1.4" fill="none"/></svg>PROTECTIVE WAX<br>FORMULA</div>
    </div>

    <aside class="specs">
      <ul class="benefits">
        <li><svg width="7" height="7" viewBox="0 0 12 12"><circle cx="6" cy="6" r="6" fill="#1d4f86"/><path d="M3.2 6.2l2 2 3.8-4" stroke="#fff" stroke-width="1.6" fill="none"/></svg><span>DEVELOPED FOR USE<br>WITH FOAM GUN<br>OR BUCKET WITH WATER</span></li>
        <li><svg width="7" height="7" viewBox="0 0 12 12"><circle cx="6" cy="6" r="6" fill="#1d4f86"/><path d="M3.2 6.2l2 2 3.8-4" stroke="#fff" stroke-width="1.6" fill="none"/></svg><span>ENHANCED SHINE</span></li>
        <li><svg width="7" height="7" viewBox="0 0 12 12"><circle cx="6" cy="6" r="6" fill="#1d4f86"/><path d="M3.2 6.2l2 2 3.8-4" stroke="#fff" stroke-width="1.6" fill="none"/></svg><span>HIGH FOAMING ACTION</span></li>
        <li><svg width="7" height="7" viewBox="0 0 12 12"><circle cx="6" cy="6" r="6" fill="#1d4f86"/><path d="M3.2 6.2l2 2 3.8-4" stroke="#fff" stroke-width="1.6" fill="none"/></svg><span>WATER REPELLENT</span></li>
        <li><svg width="7" height="7" viewBox="0 0 12 12"><circle cx="6" cy="6" r="6" fill="#1d4f86"/><path d="M3.2 6.2l2 2 3.8-4" stroke="#fff" stroke-width="1.6" fill="none"/></svg><span>STREAK FREE RINSE</span></li>
      </ul>
      <ul class="warnings">
        <li><svg width="17" height="17" viewBox="0 0 20 20"><circle cx="10" cy="10" r="9.5" fill="#1a9ae6"/><path d="M10 4v12M4.8 7l10.4 6M4.8 13l10.4-6" stroke="#fff" stroke-width="1.3"/></svg><span>KEEP FROM FREEZING</span></li>
        <li><svg width="17" height="17" viewBox="0 0 20 20"><circle cx="10" cy="10" r="9.5" fill="#1a9ae6"/><circle cx="10" cy="10" r="6.5" fill="none" stroke="#fff" stroke-width="1.2"/><path d="M5.5 14.5l9-9" stroke="#fff" stroke-width="1.2"/></svg><span>KEEP OUT OF REACH<br>OF CHILDREN</span></li>
      </ul>
      <p class="hazard">Hazardous Ingredients: NONE</p>
      <p class="notice">NOTICE: The seller and/or manufacturer assumes no responsibility for damage or injury resulting from misuse of this product. No warranties, expressed or implied, are given for the performance or safety of this product.</p>
      <p class="made">MADE IN USA</p>
    </aside>
  </section>
</div>
</body>
</html>
```